Torvel & Company: Business Cards, Stationery & Envelopes
Our Tagline is "Be Heard."
Simple
Marla Drosset
Founder, Torvel & Company
217 Meadow Lantern Dr.
Chapel Hill, North Carolina 27584
2816 Halloway Brook, NE
Atlanta, Georgia 30361
Marla@TorvelAndCo.example
www.TorvelAndCo.example
My consulting firm helps CEOs and other high-level executives with high-stakes communications. Our materials must exude professionalism and a modern, fresh, crisp and clean feel. The business cards, stationery and envelopes should match the look and feel of the logo and website. I'm interested in seeing designs that incorporate our "Be Heard" tagline, as well as ones that don't.
I think I prefer a card that is single-sided, but if you think there's a cool design that puts some information such as our addresses on back, I'm open to it.
Here are the relevant logo files

```html
<!DOCTYPE html>
<html lang="en">
<head>
<meta charset="utf-8">
<title>Torvel &amp; Company — Stationery Set</title>
<link href="https://fonts.googleapis.com/css2?family=Cinzel:wght@600&family=Open+Sans:wght@400;600&display=swap" rel="stylesheet">
<style>
  :root{
    --bg-center:#505050;
    --bg-edge:#262626;
    --paper:#ffffff;
    --paper-shade:#eeeeee;
    --red:#c8141c;
    --red-dark:#7d0a0f;
    --ink:#1a1a1a;
    --grey-text:#666666;
    --faint:#f4dcdc;
    --logo-font:'Cinzel', Georgia, serif;
    --body-font:'Open Sans', Arial, sans-serif;
  }
  *{box-sizing:border-box;margin:0;padding:0}
  html,body{width:1200px;height:346px;overflow:hidden}
  body{
    position:relative;
    background:radial-gradient(ellipse at 50% 40%, var(--bg-center), var(--bg-edge) 75%);
    font-family:var(--body-font);
    color:var(--ink);
  }
  .item{position:absolute;background:var(--paper);box-shadow:0 2px 6px rgba(0,0,0,.55);overflow:hidden}
  .corner{position:absolute;display:block}
  .corner--tl{top:0;left:0}
  .corner--br{bottom:0;right:0;transform:rotate(180deg)}
  .wordmark{font-family:var(--logo-font);font-weight:600;color:var(--ink);white-space:nowrap;display:flex;align-items:center;gap:.35em}
  .wordmark .dot{display:inline-block;width:1.1em;height:1.1em;border-radius:50%;background:var(--red)}
  .tiny{font-size:3.6px;line-height:1.45;color:var(--grey-text);white-space:nowrap}
  .faint-name{position:absolute;left:0;right:0;text-align:center;font-family:var(--logo-font);font-weight:600;color:var(--faint);white-space:nowrap}

  .brand-lockup{position:absolute;left:18px;top:86px}
  .brand-lockup .wordmark{color:#ffffff;font-size:10px}
  .brand-lockup .tagline{font-size:5px;color:#bbbbbb;margin-top:3px;margin-left:14px}

  .business-card{left:19px;top:149px;width:118px;height:72px}
  .business-card .wordmark{position:absolute;left:38px;top:14px;font-size:6.5px}
  .business-card .details{position:absolute;left:40px;top:32px}
  .business-card .person{font-size:4.6px;font-weight:600;color:var(--ink)}

  .letterhead{top:12px;width:166px;height:302px}
  .letterhead--one{left:163px}
  .letterhead--two{left:341px}
  .letterhead .wordmark{position:absolute;top:15px;font-size:6px}
  .letterhead--one .wordmark{left:38px}
  .letterhead--two .wordmark{left:48px}
  .letterhead .sender{position:absolute;left:108px;top:13px}
  .letterhead .faint-name{top:142px;font-size:12px}
  .letterhead .footer{position:absolute;left:0;right:0;bottom:16px;text-align:center}

  .envelope{left:636px;width:242px;height:110px}
  .envelope--one{top:65px}
  .envelope--two{top:202px}
  .envelope .wordmark{position:absolute;left:30px;top:10px;font-size:6.5px}
  .envelope .return{position:absolute;left:32px;top:24px}
  .envelope .footer{position:absolute;left:0;right:0;bottom:8px;text-align:center}

  .envelope-back svg{position:absolute;inset:0}
  .envelope-back--dark{top:55px;height:77px;left:905px;width:276px;background:#151515}
  .envelope-back--red{top:120px;height:103px;left:914px;width:267px;background:linear-gradient(180deg,var(--red),var(--red-dark))}
  .envelope-back--white{top:214px;height:100px;left:900px;width:281px;background:var(--paper)}
  .seal{position:absolute;width:24px;height:24px;border-radius:50%;left:50%;transform:translateX(-50%)}
  .envelope-back--dark .seal{top:22px;background:#ffffff}
  .envelope-back--red .seal{top:26px;background:var(--paper)}
  .envelope-back--red .seal::after{content:"";position:absolute;inset:6px;border-radius:50%;background:var(--red)}
</style>
</head>
<body>

<svg width="0" height="0" style="position:absolute" aria-hidden="true">
  <defs>
    <symbol id="swoosh" viewBox="0 0 100 60">
      <path d="M0 0 H70 Q30 8 0 46 Z" fill="var(--red)"/>
      <path d="M0 46 Q30 8 70 0 H80 Q34 10 0 54 Z" fill="var(--ink)"/>
    </symbol>
  </defs>
</svg>

<div class="brand-lockup">
  <div class="wordmark"><span class="dot"></span>Torvel &amp; Company</div>
  <div class="tagline">Be Heard.</div>
</div>

<div class="item business-card">
  <svg class="corner corner--tl" width="44" height="26"><use href="#swoosh"/></svg>
  <svg class="corner corner--br" width="30" height="18"><use href="#swoosh"/></svg>
  <div class="wordmark"><span class="dot"></span>Torvel &amp; Company</div>
  <div class="details">
    <div class="person">Marla Drosset</div>
    <div class="tiny">Founder, Torvel &amp; Company</div>
    <div class="tiny">Marla@TorvelAndCo.example</div>
    <div class="tiny">www.TorvelAndCo.example</div>
  </div>
</div>

<div class="item letterhead letterhead--one">
  <svg class="corner corner--tl" width="60" height="36"><use href="#swoosh"/></svg>
  <svg class="corner corner--br" width="60" height="36"><use href="#swoosh"/></svg>
  <div class="wordmark"><span class="dot"></span>Torvel &amp; Co.</div>
  <div class="sender">
    <div class="tiny">217 Meadow Lantern Dr.</div>
    <div class="tiny">Chapel Hill, NC 27584</div>
    <div class="tiny">Marla@TorvelAndCo.example</div>
  </div>
  <div class="faint-name">Torvel &amp; Company</div>
  <div class="footer tiny">www.TorvelAndCo.example</div>
</div>

<div class="item letterhead letterhead--two">
  <svg class="corner corner--tl" width="60" height="36"><use href="#swoosh"/></svg>
  <svg class="corner corner--br" width="60" height="36"><use href="#swoosh"/></svg>
  <div class="wordmark"><span class="dot"></span>Torvel &amp; Company</div>
  <div class="faint-name">Torvel &amp; Company</div>
  <div class="footer tiny">2816 Halloway Brook, NE · Atlanta, Georgia 30361 · www.TorvelAndCo.example</div>
</div>

<div class="item envelope envelope--one">
  <svg class="corner corner--tl" width="40" height="24"><use href="#swoosh"/></svg>
  <svg class="corner corner--br" width="40" height="24"><use href="#swoosh"/></svg>
  <div class="wordmark"><span class="dot"></span>Torvel &amp; Company</div>
  <div class="return">
    <div class="tiny">217 Meadow Lantern Dr., Chapel Hill, North Carolina 27584</div>
  </div>
</div>

<div class="item envelope envelope--two">
  <svg class="corner corner--tl" width="40" height="24"><use href="#swoosh"/></svg>
  <svg class="corner corner--br" width="40" height="24"><use href="#swoosh"/></svg>
  <div class="wordmark"><span class="dot"></span>Torvel &amp; Company</div>
  <div class="footer tiny">2816 Halloway Brook, NE · Atlanta, Georgia 30361</div>
</div>

<div class="item envelope-back envelope-back--dark">
  <svg viewBox="0 0 276 77" preserveAspectRatio="none" aria-hidden="true">
    <path d="M0 0 L138 46 L276 0" fill="#000" stroke="#333" stroke-width="1"/>
  </svg>
  <span class="seal"></span>
</div>

<div class="item envelope-back envelope-back--red">
  <svg viewBox="0 0 267 103" preserveAspectRatio="none" aria-hidden="true">
    <path d="M0 0 L133 54 L267 0 Z" fill="rgba(0,0,0,.35)"/>
    <path d="M0 103 L120 50 M267 103 L146 50" stroke="rgba(0,0,0,.25)" stroke-width="1" fill="none"/>
  </svg>
  <span class="seal"></span>
</div>

<div class="item envelope-back envelope-back--white">
  <svg viewBox="0 0 281 100" preserveAspectRatio="none" aria-hidden="true">
    <path d="M0 0 L140 52 L281 0" fill="var(--paper-shade)" stroke="#cfcfcf" stroke-width="1"/>
    <path d="M0 100 L124 46 M281 100 L156 46" stroke="#d6d6d6" stroke-width="1" fill="none"/>
  </svg>
</div>

</body>
</html>
```